Card for modern wood artisan that builds log homes and timber frames.

Design a card with catchy imagery. With a quick list of things I build and services I offer.

I'd like an English side and a french side. I can provide the text.

I am basically a guy that builds log homes and timber frames , but I am very eco friendly oriented.

I use only eco friendly products to limit my carbon footprint.
I want the client to feel as if they are hiring a good smart builder.

I have been building for a while but just starting out to market myself out there , not just work for other companies. Starting
My own thing legitimately.

I am very conscientious, and I take care of the work I do. I am trying to bring a new age, modern feel to an old profession.

Reason: I am not completely satisfied with A model yet, looking for that masculin rustic artistic design that I havent completely found yet. Thank you for your sumbissions.

Target Market(s)

People looking to hire a builder to design and build their projects.
And contractors that want to hire a quality subcontractor for their jobs.

Industry/Entity Type

Construction

Contact Information for Business Card

I want my logo on it, that I had designed here.
And a list of services I provide.

With my phone number, website adress and Email.

Requirements
Must have
• Artful presentation,
• Eco friendly feel
• I love trees.

```html
<!DOCTYPE html>
<html lang="en">
<head>
<meta charset="utf-8">
<title>Bérard — Wood Artisan Cards</title>
<link rel="stylesheet" href="https://fonts.googleapis.com/css2?family=Oswald:wght@400;700&family=Open+Sans:wght@700;800&family=Bebas+Neue&display=swap">
<style>
  :root {
    --page: #ece8e1;
    --kraft: #d9cfbb;
    --kraft-edge: #c7bba3;
    --ink: #1d1b18;
    --tree: rgba(230, 207, 60, 0.75);
    --tree-fade: rgba(230, 207, 60, 0);
    --grain: #23201c;
  }
  * { box-sizing: border-box; margin: 0; padding: 0; }
  html, body { width: 974px; height: 1200px; overflow: hidden; background: var(--page); }
  .sheet { position: relative; width: 974px; height: 1200px; }
  .card-side { position: absolute; top: 150px; width: 420px; }
  .card-side.french { left: 47px; }
  .card-side.english { left: 507px; }
  .card {
    position: relative; width: 420px; height: 735px; overflow: hidden;
    background: var(--kraft); border: 1px solid var(--kraft-edge);
    box-shadow: 0 6px 18px rgba(0,0,0,0.18);
    color: var(--ink); text-align: center;
  }
  .founder-badge { position: absolute; left: 100px; top: 0; width: 220px; height: 170px; }
  .founder-badge svg { position: absolute; inset: 0; }
  .founder-name {
    position: absolute; left: 0; right: 0; top: 70px;
    font: 700 30px/1 "Oswald", sans-serif; letter-spacing: 1px;
  }
  .founder-year {
    position: absolute; left: 0; right: 0; top: 110px;
    font: 400 14px/1 "Oswald", sans-serif; letter-spacing: 2px;
  }
  .tree-art {
    position: absolute; left: 100px; top: 180px; width: 220px; height: 320px;
    background: radial-gradient(ellipse 50% 50% at 50% 45%, var(--tree) 0%, var(--tree) 45%, var(--tree-fade) 100%);
  }
  .brand { position: absolute; left: 0; right: 0; top: 222px; display: flex; justify-content: center; align-items: center; gap: 14px; }
  .brand-square { width: 40px; height: 40px; background: var(--ink); }
  .brand-name { font: 700 54px/1 "Oswald", sans-serif; letter-spacing: 2px; }
  .tagline { position: absolute; left: 0; right: 0; top: 290px; font: 400 17px/1 "Oswald", sans-serif; letter-spacing: 1px; }
  .services { position: absolute; left: 0; right: 0; top: 360px; list-style: none; font: 800 21px/1.3 "Open Sans", sans-serif; }
  .contact { position: absolute; left: 0; right: 0; top: 500px; font: 700 19px/1.45 "Open Sans", sans-serif; }
  .contact .phone { font-size: 27px; font-weight: 800; margin-bottom: 4px; }
  .wood-corner {
    position: absolute; right: 0; bottom: 0; width: 130px; height: 130px;
    background: linear-gradient(135deg, #3a342c, var(--grain));
    clip-path: polygon(100% 0, 100% 100%, 0 100%);
  }
  .side-label {
    margin-top: 26px; text-align: right;
    font: 400 44px/1 "Bebas Neue", sans-serif; letter-spacing: 2px; color: var(--ink);
  }
</style>
</head>
<body>
<main class="sheet">

  <section class="card-side french" lang="fr">
    <article class="card">
      <div class="founder-badge">
        <svg viewBox="0 0 220 170" width="220" height="170" aria-hidden="true">
          <polyline points="3,0 3,120 110,167 217,120 217,0" fill="none" stroke="var(--ink)" stroke-width="3"/>
          <line x1="70" y1="118" x2="150" y2="118" stroke="var(--ink)" stroke-width="1"/>
        </svg>
        <p class="founder-name">LUC BÉRARD</p>
        <p class="founder-year">2017</p>
      </div>
      <div class="tree-art" role="img" aria-label="Yellow sketched tree illustration"></div>
      <div class="brand"><span class="brand-square"></span><span class="brand-name">BÉRARD</span></div>
      <p class="tagline">ARTISAN DE BOIS</p>
      <ul class="services">
        <li>SERVICES DE MENUISERIE</li>
        <li>MAISON DE BOIS</li>
        <li>CONSTRUCTION</li>
        <li>CADRE EN BOIS</li>
      </ul>
      <div class="contact">
        <p class="phone">555.010.0000</p>
        <p>BUILDER@BERARDBOIS.COM</p>
        <p>WWW.BERARDBOIS.COM</p>
      </div>
      <div class="wood-corner" role="img" aria-label="Black wood grain pattern corner"></div>
    </article>
    <p class="side-label">FRENCH SIDE</p>
  </section>

  <section class="card-side english" lang="en">
    <article class="card">
      <div class="founder-badge">
        <svg viewBox="0 0 220 170" width="220" height="170" aria-hidden="true">
          <polyline points="3,0 3,120 110,167 217,120 217,0" fill="none" stroke="var(--ink)" stroke-width="3"/>
          <line x1="70" y1="118" x2="150" y2="118" stroke="var(--ink)" stroke-width="1"/>
        </svg>
        <p class="founder-name">LUC BÉRARD</p>
        <p class="founder-year">2017</p>
      </div>
      <div class="tree-art" role="img" aria-label="Yellow sketched tree illustration"></div>
      <div class="brand"><span class="brand-square"></span><span class="brand-name">BÉRARD</span></div>
      <p class="tagline">WOOD ARTISAN</p>
      <ul class="services">
        <li>CARPENTRY SERVICES</li>
        <li>LOG HOME</li>
        <li>CONSTRUCTION</li>
        <li>TIMBER FRAME</li>
      </ul>
      <div class="contact">
        <p class="phone">555.010.0000</p>
        <p>BUILDER@BERARDBOIS.COM</p>
        <p>WWW.BERARDBOIS.COM</p>
      </div>
      <div class="wood-corner" role="img" aria-label="Black wood grain pattern corner"></div>
    </article>
    <p class="side-label">ENGLISH SIDE</p>
  </section>

</main>
</body>
</html>
```